Innovative Veterinary Clinic Business Card

We are a mixed animal veterinary practice in rural Queensland. Our patients include cattle, horses, dogs and cats, with everything in between. We are moving the clinic forward to become the best in our region and one of the best in the State, with gold standard service and standards of care, while remaining down to earth and genuine. Our current motto is - "Every patient comes first". The clinic colours are blue and red but am open to change. I would like something innovative and modern, that stands out and says we are different, we are amazing, and our patients come first. Something that will be remembered. Our current logo and business card I feel are empty and don't stand out.
Updates

please use font that is strong but simple. I am looking for something different, rather than your run of the mill business card. I am open to anything - as long as it has two sides and defines us, I'll consider all submissions. Thank you for your efforts, they are all very much appreciated!!

Thank you all very much for your amazing efforts. I wasn't expecting to have such a great response, so I thank you for your participation. You are all very talented and I loved your designs. I wish you all the best for the future. Thank you!

Target Market(s)

pet owners, graziers, horse clients (horses of all types - pets, campdrafting, mustering, polocrosse, thoroughbreds, show ponies)

Industry/Entity Type

Veterinary

Contact Information for Business Card

Dr. Freya L Tovell - BVSc (Hons)
Creekbend Veterinary Services
17 Harrow St
Wattleford, QLD, 4692
Ph: 0741872306 or 0418365947
Fax: 0741872309
e: creekbendvets@mailnest.example

Colors

Designer to choose colors to be used in the design.

Requirements
Must have
• back side of card to be used as an appointment card
Nice to have
• perhaps a photo of an animal (horse, dog, cat, cattle)
Should not have
• I don't want the standard name, rank and serial number business card. No cartoon animals.

```html
<!DOCTYPE html>
<html lang="en">
<head>
<meta charset="utf-8">
<title>Creekbend Veterinary Services – Business &amp; Appointment Card</title>
<link href="https://fonts.googleapis.com/css2?family=Montserrat:wght@400;600;700&display=swap" rel="stylesheet">
<style>
  :root {
    --clinic-blue: #4a68b3;
    --clinic-red: #6b0f0f;
    --paper: #ffffff;
    --backdrop: #8d9fcf;
    --field-line: #4a68b3;
  }
  * { box-sizing: border-box; margin: 0; padding: 0; }
  html, body { width: 1200px; height: 1000px; overflow: hidden; }
  body {
    background: var(--backdrop);
    font-family: "Montserrat", sans-serif;
    position: relative;
  }
  .card {
    position: absolute;
    width: 360px;
    height: 550px;
    background: var(--paper);
    overflow: hidden;
    box-shadow: 0 2px 6px rgba(0,0,0,0.25);
  }
  .card--front { left: 188px; top: 82px; }
  .card--back { left: 618px; top: 355px; height: 548px; }
  .card__shape { position: absolute; left: 0; top: 0; }

  /* Front */
  .brand {
    position: absolute; left: 0; top: 164px; width: 360px;
    text-align: center;
  }
  .brand__name {
    color: var(--clinic-blue);
    font-weight: 700;
    font-size: 21px;
    line-height: 24px;
    letter-spacing: 0.5px;
    text-transform: uppercase;
  }
  .brand__motto {
    margin-top: 8px;
    color: var(--clinic-red);
    font-size: 11px;
    letter-spacing: 2.2px;
    text-transform: uppercase;
  }
  .address {
    position: absolute; left: 0; top: 258px; width: 360px;
    text-align: center;
    color: var(--clinic-blue);
    font-style: normal;
    font-weight: 600;
    font-size: 15px;
    line-height: 29px;
    letter-spacing: 1px;
  }
  .contacts { position: absolute; left: 24px; top: 353px; list-style: none; }
  .contacts__item {
    display: flex; align-items: center;
    height: 37px;
    color: #fff;
    font-size: 15px;
    letter-spacing: 0.3px;
  }
  .contacts__icon { width: 30px; height: 22px; margin-right: 16px; fill: #fff; flex: none; }
  .contacts__or { color: var(--clinic-red); margin: 0 5px; }
  .practitioner {
    position: absolute; left: 0; top: 490px; width: 360px; height: 30px;
    background: var(--clinic-red);
    border-top: 2px solid #a66a6a;
    border-bottom: 2px solid #a66a6a;
    color: #fff;
    font-weight: 600;
    font-size: 15px;
    letter-spacing: 1.3px;
    text-align: center;
    line-height: 26px;
  }

  /* Back */
  .appointment-title {
    position: absolute; left: 0; top: 10px;
    color: #fff;
    font-weight: 700;
    font-size: 23px;
    line-height: 21px;
  }
  .appointment-title span { display: block; }
  .appointment-title__line1 { margin-left: 47px; }
  .appointment-title__line2 { margin-left: 115px; }
  .field {
    position: absolute; left: 8px;
    display: flex; align-items: flex-end;
    color: var(--clinic-red);
    font-weight: 700;
    font-size: 15px;
    line-height: 20px;
  }
  .field__line {
    height: 3px;
    background: var(--field-line);
    margin-left: 10px;
  }
  .field--pet { top: 128px; }
  .field--pet .field__line { width: 278px; }
  .field--date { top: 210px; }
  .field--date .field__line { width: 280px; }
  .field--time { top: 272px; }
  .field--time .field__line { width: 280px; }
  .back-brand {
    position: absolute; left: 125px; top: 372px; width: 140px;
    text-align: center;
    color: var(--clinic-blue);
    font-weight: 700;
    font-size: 8px;
    line-height: 10px;
    text-transform: uppercase;
  }
  .back-brand__motto {
    display: block;
    margin-top: 2px;
    color: var(--clinic-red);
    font-weight: 400;
    font-size: 5px;
    letter-spacing: 0.8px;
  }
  .animal-photo {
    position: absolute; left: 0; top: 405px; width: 360px; height: 143px;
    background: linear-gradient(90deg, #6b3a1f 0%, #8a5230 28%, #3a2a20 42%, #a48860 55%, #b5672f 75%, #c07a45 100%);
  }
</style>
</head>
<body>

<section class="card card--front" aria-label="Business card front">
  <svg class="card__shape" width="360" height="550" viewBox="0 0 360 550">
    <path d="M0 312 C 90 318, 250 338, 360 310 L360 550 L0 550 Z" fill="var(--clinic-red)"/>
    <path d="M0 322 C 100 330, 250 345, 360 320 L360 550 L0 550 Z" fill="var(--clinic-blue)"/>
  </svg>

  <div class="brand">
    <div class="brand__name">Creekbend Veterinary<br>Services</div>
    <div class="brand__motto">Every patient comes first</div>
  </div>

  <address class="address">
    17 Harrow St Wattleford<br>QLD, 4692
  </address>

  <ul class="contacts">
    <li class="contacts__item">
      <svg class="contacts__icon" viewBox="0 0 30 22" aria-label="Phone"><path d="M2 8 C2 2 28 2 28 8 L23 9 L22 6 C18 4.5 12 4.5 8 6 L7 9 Z"/><rect x="5" y="11" width="20" height="10" rx="2"/><circle cx="15" cy="16" r="3" fill="var(--clinic-blue)"/></svg>
      0741872306<span class="contacts__or">or</span>0418365947
    </li>
    <li class="contacts__item">
      <svg class="contacts__icon" viewBox="0 0 30 22" aria-label="Fax"><path d="M8 1 H22 V9 H8 Z M10 3 V7 H20 V3 Z" fill-rule="evenodd"/><path d="M3 10 H27 V21 H3 Z M6 13 V15 H24 V13 Z M6 17 V19 H24 V17 Z" fill-rule="evenodd"/></svg>
      0741872309
    </li>
    <li class="contacts__item">
      <svg class="contacts__icon" viewBox="0 0 30 22" aria-label="Email"><path d="M2 3 H28 V19 H2 Z"/><path d="M2 3 L15 13 L28 3" fill="none" stroke="var(--clinic-blue)" stroke-width="1.8"/></svg>
      creekbendvets@mailnest.example
    </li>
  </ul>

  <div class="practitioner">Dr. Freya L Tovell, BVSc (Hons)</div>
</section>

<section class="card card--back" aria-label="Appointment card back">
  <svg class="card__shape" width="360" height="548" viewBox="0 0 360 548">
    <path d="M0 0 H360 V125 C 260 80, 120 55, 0 115 Z" fill="var(--clinic-blue)"/>
    <path d="M0 108 C 120 50, 260 78, 360 118 L360 128 C 260 90, 120 68, 0 122 Z" fill="var(--clinic-red)"/>
  </svg>

  <h2 class="appointment-title">
    <span class="appointment-title__line1">Your pet has</span>
    <span class="appointment-title__line2">an appointment:</span>
  </h2>

  <div class="field field--pet"><span>Pet's<br>Name:</span><span class="field__line"></span></div>
  <div class="field field--date"><span>Date:</span><span class="field__line"></span></div>
  <div class="field field--time"><span>Time:</span><span class="field__line"></span></div>

  <div class="back-brand">Creekbend Veterinary Services<span class="back-brand__motto">Every patient comes first</span></div>

  <div class="animal-photo" role="img" aria-label="Photo of a horse, a dog, a cat and a red cow side by side"></div>
</section>

</body>
</html>
```